RVK Entertainment

Logo for business card design

Target Market(s)

potential film investors and screenwriters

Industry/Entity Type

Business

Contact Information for Business Card

as shown, website here is a placeholder position

Requirements
Must have
• great visual appeal
Nice to have
• harmony of colors; must evoke spirit of
• U.S.-China cooperation

```html
<!DOCTYPE html>
<html lang="en">
<head>
<meta charset="utf-8">
<title>RVK Entertainment — Business Card</title>
<link rel="stylesheet" href="https://fonts.googleapis.com/css2?family=Oswald:wght@400;500&display=swap">
<style>
  :root {
    --card-center: #3b3b3b;
    --card-edge: #141414;
    --text-light: #ffffff;
    --accent-yellow: #fff200;
    --divider: #d9d9d9;
  }
  * { margin: 0; padding: 0; box-sizing: border-box; }
  html, body {
    width: 1200px;
    height: 686px;
    overflow: hidden;
    background: var(--card-edge);
  }
  .business-card {
    position: relative;
    width: 1200px;
    height: 686px;
    background: radial-gradient(circle at 50% 40%, var(--card-center) 0%, #262626 45%, var(--card-edge) 100%);
    font-family: "Oswald", "Arial Narrow", sans-serif;
    color: var(--text-light);
    overflow: hidden;
  }
  .brand {
    position: absolute;
    top: 150px;
    left: 0;
    width: 100%;
    text-align: center;
    color: var(--text-light);
    font-weight: 500;
    text-transform: uppercase;
  }
  .brand-name {
    display: block;
    font-size: 150px;
    line-height: 150px;
    letter-spacing: 10px;
  }
  .brand-tagline {
    display: block;
    margin-top: 14px;
    font-size: 40px;
    line-height: 40px;
    letter-spacing: 25px;
    padding-left: 25px;
  }
  .contact {
    position: absolute;
    top: 460px;
    font-size: 29px;
    line-height: 42px;
    letter-spacing: 2.5px;
    text-transform: uppercase;
    font-weight: 400;
  }
  .contact-details { left: 71px; }
  .contact-address { right: 81px; text-align: right; }
  .contact-divider {
    position: absolute;
    left: 729px;
    top: 463px;
    width: 2px;
    height: 116px;
    background: var(--divider);
  }
  .accent-band {
    position: absolute;
    left: 0;
    top: 619px;
    width: 100%;
    height: 25px;
    background: var(--accent-yellow);
  }
</style>
</head>
<body>
  <div class="business-card">
    <div class="brand">
      <span class="brand-name">RVK</span>
      <span class="brand-tagline">Entertainment</span>
    </div>

    <div class="contact contact-details">
      <p>Website: www.rvkentertainment.com</p>
      <p>Email: www.rvkentertainment.com</p>
      <p>Phone: 000-000-0000</p>
    </div>

    <div class="contact-divider"></div>

    <div class="contact contact-address">
      <p>1280 Harbor Way #210,</p>
      <p>Laguna Vista,</p>
      <p>California 92700 USA</p>
    </div>

    <div class="accent-band"></div>
  </div>
</body>
</html>
```